The Nine Lanterns CD cover and booklet - meditation walks

I have created a CD of five meditation walks for the modern mystic - with a professional voice over and really cool music - to help people find their way back home to their true Self. It is very powerful and life-enhancing. The walks were created on the Canary Island of Lanzarote in Bartolo's garden and I have stunning photographs taken by pro-photographer Owen Fairbrook to accompany the sleeve notes. The result will be a truly beautiful 12pp CD sleeve note booklet - which will itself be so cleanly laid out people will want to pick it up and play! :-) You can do that for me ... and, of course, you will get a free signed copy of the finished CD ... Rudy - The Nine Lanterns - see http://www.thewellspring-example.com/
I will send a CD page layout template, the full text and hi-res images to the selected design partner. I attach sample text docs and lo-res logo.
Extra guaranteed money and extended deadline with helpful files.
Hi there - I'm very excited about what designs I get for The Nine Lanterns CD. Everything is ready to go!
Rudy
Today I have uploaded a hi-res version of The Nine Lanterns logo which you may find helpful.
Rudy
Several designers have requested hi-res images of the pictures on the PDF sample pages - so I have uploaded this evening some additional hi-res images as well as a hi-res logo.
hi all you lovely designers! Today is the last day for submission of designs - so if you want a shout ... its now or never. :-)

```html
<!DOCTYPE html>
<html lang="en">
<head>
<meta charset="utf-8">
<title>The Nine Lanterns – CD Sleeve</title>
<link rel="stylesheet" href="https://fonts.googleapis.com/css2?family=Arimo:wght@400;700&family=Questrial&family=Kalam:wght@400;700&display=swap">
<style>
  :root{
    --paper:#ffffff;
    --frame:#b9bfe0;
    --brown:#a98470;
    --teal:#3f7f96;
    --teal-dark:#2f6f87;
    --sea:#37c6c9;
    --sea-deep:#1aa9b3;
    --sand:#c39a77;
    --logo-blue:#1f5f8a;
  }
  *{margin:0;padding:0;box-sizing:border-box}
  html,body{width:1200px;height:900px;overflow:hidden;background:var(--paper)}
  .canvas{position:relative;width:1200px;height:900px;background:var(--paper)}
  .sleeve{position:absolute;left:42px;top:173px;width:1115px;height:553px;border:1px solid var(--frame)}
  .fold{position:absolute;left:557px;top:0;height:100%;border-left:1px dashed #9a9a9a}
  .abs{position:absolute;white-space:nowrap}

  /* back panel */
  .back-photo{left:0;top:0;width:236px;height:353px;background:linear-gradient(160deg,var(--sea) 0%,var(--sea-deep) 100%)}
  .tracks-title{left:264px;top:14px;font:400 27px/1 'Kalam',cursive;color:var(--brown)}
  .tracks{left:264px;top:62px;width:262px;list-style:none;font:400 17px/26px 'Kalam',cursive;color:var(--brown)}
  .tracks li{display:flex;justify-content:space-between}
  .back-quote{left:262px;top:252px;font:400 18px/25px 'Kalam',cursive;color:var(--teal)}
  .back-quote cite{display:block;text-align:right;font-style:normal;margin-top:8px;width:262px;color:var(--teal)}
  .blurb{left:27px;top:364px;width:503px;white-space:normal;font:400 14.5px/20px 'Questrial',sans-serif;color:var(--brown);letter-spacing:.3px}
  .publisher{left:26px;top:431px;width:167px;height:73px;border:3px solid var(--teal);display:flex;align-items:center;justify-content:center;font:400 12px 'Arimo',sans-serif;color:var(--teal-dark)}
  .web{left:222px;top:460px;font:400 13px 'Questrial',sans-serif;color:var(--brown);letter-spacing:.2px}
  .brand{display:flex;align-items:center;gap:6px;font:700 13px 'Arimo',sans-serif;color:var(--logo-blue)}
  .brand .mark{width:14px;height:14px;background:var(--logo-blue)}
  .brand-back{left:462px;top:470px}
  .credit{left:24px;top:517px;font:400 12px 'Arimo',sans-serif;color:var(--teal-dark);letter-spacing:-.1px}

  /* front panel */
  .title{left:587px;top:36px;font:700 34px/1 'Arimo',sans-serif;color:var(--brown)}
  .rules{left:966px;top:38px}
  .subtitle{left:588px;top:78px;font:400 21px/1 'Arimo',sans-serif;color:var(--teal);letter-spacing:.3px}
  .tagline{left:587px;top:106px;font:700 17px/1 'Kalam',cursive;color:var(--teal)}
  .band-line{left:557px;width:558px;height:3px;background:var(--teal)}
  .front-photo{left:557px;top:164px;width:558px;height:266px;background:linear-gradient(180deg,#5b8ea8 0%,#8fb7c6 30%,#e2e7e4 48%,#d6b79a 62%,var(--sand) 100%)}
  .front-quote{left:583px;top:353px;font:400 16px/23px 'Kalam',cursive;color:#fff}
  .front-quote cite{font-style:normal;font-size:17px;margin-left:48px}
  .rules-bottom{left:557px;top:494px}
  .created{right:154px;top:460px;text-align:right;color:var(--brown)}
  .created .by{font:400 23px/1 'Arimo',sans-serif;color:var(--teal)}
  .created .name{font:400 29px/1 'Arimo',sans-serif;margin-top:8px}
  .brand-front{left:992px;top:480px}
</style>
</head>
<body>
<div class="canvas">
  <div class="sleeve">
    <div class="fold"></div>

    <section class="back">
      <div class="abs back-photo" role="img" aria-label="Photo of footprints seen through clear turquoise shallow water"></div>
      <h2 class="abs tracks-title">the Nine Lanterns</h2>
      <ol class="abs tracks">
        <li><span>1 . Introduction</span><span>3:52</span></li>
        <li><span>2. Via Positiva</span><span>9:04</span></li>
        <li><span>3 .Via Negativa</span><span>6:54</span></li>
        <li><span>4 .Via Creativa</span><span>6:22</span></li>
        <li><span>5. Via Transformativa</span><span>5:52</span></li>
        <li><span>6. Via Integrativa</span><span>4:53</span></li>
      </ol>
      <blockquote class="abs back-quote">“What you are looking for<br>&nbsp;is what is looking.”<cite>Brother Anselm</cite></blockquote>
      <p class="abs blurb">These walking meditations created in Bartolo’s garden, Lanzarote will make you feel grounded and uplifted, centred and expansive, connected with your deepest purpose and your true Self.</p>
      <div class="abs publisher">© Tidewater Publishing 2013</div>
      <div class="abs web">www.theninelanterns-example.com</div>
      <div class="abs brand brand-back"><span class="mark"></span>Tidewater</div>
      <p class="abs credit">Photo: Playa de las Conchas, La Graciosa, Lanzarote, Canary Islands &nbsp;by Owen Fairbrook, kp3.</p>
    </section>

    <section class="front">
      <h1 class="abs title">THE NINE LANTERNS</h1>
      <svg class="abs rules" width="149" height="32" viewBox="0 0 149 32" aria-hidden="true">
        <g stroke="#a98470" stroke-width="1.5">
          <line x1="0" y1="2" x2="149" y2="2"/><line x1="0" y1="9" x2="149" y2="9"/>
          <line x1="0" y1="16" x2="149" y2="16"/><line x1="0" y1="23" x2="149" y2="23"/>
          <line x1="0" y1="30" x2="149" y2="30"/>
        </g>
      </svg>
      <p class="abs subtitle">WALKING MEDITATIONS</p>
      <p class="abs tagline">for the mystic in you</p>
      <div class="abs band-line" style="top:158px"></div>
      <div class="abs front-photo" role="img" aria-label="Photo of a beach with breaking waves, a distant figure in the surf and footprints in the sand"></div>
      <blockquote class="abs front-quote">“You find out that what you’ve been searching for<br>you already are.” <cite>Marlow Reyes</cite></blockquote>
      <div class="abs band-line" style="top:430px;height:2px;background:#fff;border-bottom:1px solid var(--teal)"></div>
      <svg class="abs rules-bottom" width="194" height="24" viewBox="0 0 194 24" aria-hidden="true">
        <g stroke="#a98470" stroke-width="1.5">
          <line x1="0" y1="2" x2="194" y2="2"/><line x1="0" y1="7" x2="194" y2="7"/>
          <line x1="0" y1="12" x2="194" y2="12"/><line x1="0" y1="17" x2="194" y2="17"/>
          <line x1="0" y1="22" x2="194" y2="22"/>
        </g>
      </svg>
      <div class="abs created">
        <div class="by">created by</div>
        <div class="name">Rudy Calloway</div>
      </div>
      <div class="abs brand brand-front"><span class="mark"></span>Tidewater</div>
    </section>
  </div>
</div>
</body>
</html>
```